Card design for orthopaedic surgeons working as The Brindlewood Orthopaedic Centre

Business cards, letterhead

Colors

Designer to choose colors to be used in the design.

Requirements
Must have
• Late addition.
• Cards letterhead must have logos of
• Corvane Federated Institute of Surgeons
• Meridale Orthopaedic Society
Nice to have
• Back of card to have space for appointment time to be added by hand and some blank space for writing incidental other notes.

```html
<!DOCTYPE html>
<html lang="en">
<head>
<meta charset="utf-8">
<title>The Brindlewood Orthopaedic Centre — Business Card</title>
<link href="https://fonts.googleapis.com/css2?family=Montserrat:wght@400;500;600&display=swap" rel="stylesheet">
<style>
  :root {
    --backdrop: #1c1c1e;
    --navy: #06324a;
    --sky: #4a9fd4;
    --paper: #ededee;
    --paper-light: #f4f4f5;
    --ink: #555a5e;
    --rule: #9a9a9a;
    --badge: #d6dde3;
    --white: #ffffff;
  }
  * { margin: 0; padding: 0; box-sizing: border-box; }
  html, body {
    width: 1200px; height: 900px; overflow: hidden;
    background: var(--backdrop);
    font-family: "Montserrat", sans-serif;
  }
  .stage { position: relative; width: 1200px; height: 900px; }

  .card {
    position: absolute; left: 332px; width: 555px; height: 317px;
    overflow: hidden;
  }
  .card--front { top: 125px; background: var(--navy); }
  .card--back {
    top: 479px;
    background: linear-gradient(120deg, var(--paper) 0%, var(--paper-light) 100%);
  }

  .wordmark {
    position: absolute; white-space: nowrap; line-height: 1;
    font-weight: 400; letter-spacing: -0.6px; word-spacing: -2px;
  }
  .card--front .wordmark {
    left: 0; right: 0; text-align: center; top: 168px;
    font-size: 22px; color: var(--white);
  }
  .card--back .wordmark {
    left: 34px; top: 71px; font-size: 17px; color: var(--navy);
  }

  .affiliations {
    position: absolute; right: 29px; top: 58px;
    display: flex; gap: 10px;
  }
  .affiliations__badge {
    width: 40px; height: 40px; border-radius: 50%;
    background: var(--badge);
  }

  .person { position: absolute; left: 34px; top: 147px; line-height: 1; }
  .person__name { font-size: 23px; font-weight: 600; color: var(--navy); letter-spacing: 0.3px; }
  .person__role { margin-top: 5px; font-size: 15px; font-weight: 400; color: var(--ink); }

  .divider {
    position: absolute; left: 34px; top: 199px; width: 492px; height: 1.5px;
    background: var(--rule);
  }

  .contacts { position: absolute; left: 34px; top: 209px; list-style: none; }
  .contacts li {
    display: flex; align-items: center; height: 19px;
    font-size: 13px; color: var(--ink); letter-spacing: 0.3px;
  }
  .contacts svg { width: 12px; height: 12px; margin-right: 9px; fill: var(--sky); flex: none; }

  .address {
    position: absolute; right: 31px; top: 229px; text-align: right;
    font-size: 13px; line-height: 18px; color: var(--ink); letter-spacing: 0.3px;
    font-style: normal;
  }

  .footer-bands { position: absolute; left: 0; bottom: 0; width: 555px; height: 29px; }
  .website {
    position: absolute; right: 30px; bottom: 8px; line-height: 1;
    font-size: 12.5px; color: var(--white); letter-spacing: 0.4px;
  }
</style>
</head>
<body>
<main class="stage">

  <section class="card card--front" aria-label="Card front">
    <p class="wordmark">The Brindlewood Orthopaedic Centre</p>
  </section>

  <section class="card card--back" aria-label="Card back">
    <p class="wordmark">The Brindlewood Orthopaedic Centre</p>

    <div class="affiliations">
      <div class="affiliations__badge" role="img" aria-label="Corvane Federated Institute of Surgeons membership badge"></div>
      <div class="affiliations__badge" role="img" aria-label="Meridale Orthopaedic Society membership badge"></div>
    </div>

    <div class="person">
      <h1 class="person__name">Adrien Kell</h1>
      <p class="person__role">Director</p>
    </div>

    <div class="divider"></div>

    <ul class="contacts">
      <li>
        <svg viewBox="0 0 24 24" aria-hidden="true"><path d="M6.6 10.8a15.1 15.1 0 0 0 6.6 6.6l2.2-2.2a1 1 0 0 1 1-.25 11.4 11.4 0 0 0 3.6.57 1 1 0 0 1 1 1V20a1 1 0 0 1-1 1A17 17 0 0 1 3 4a1 1 0 0 1 1-1h3.5a1 1 0 0 1 1 1c0 1.250.2 2.45.57 3.57a1 1 0 0 1-.25 1z"/></svg>
        03 5550 1842
      </li>
      <li>
        <svg viewBox="0 0 24 24" aria-hidden="true"><path d="M7 1h10a2 2 0 0 1 2 2v18a2 2 0 0 1-2 2H7a2 2 0 0 1-2-2V3a2 2 0 0 1 2-2zm0 3v14h10V4zm5 15.5a1.2 1.2 0 1 0 0 2.4 1.2 1.2 0 0 0 0-2.4z"/></svg>
        0491 570 226
      </li>
      <li>
        <svg viewBox="0 0 24 24" aria-hidden="true"><path d="M2 5h20v2l-10 6L2 7zm0 4.3 10 6 10-6V19H2z"/></svg>
        hello@brindlewoodortho.com
      </li>
    </ul>

    <address class="address">
      Level 2, 17 Harlow Lane<br>
      Fenmore, VIC 3999
    </address>

    <svg class="footer-bands" viewBox="0 0 555 29" aria-hidden="true">
      <polygon points="0,16 326,16 317,29 0,29" fill="var(--sky)"/>
      <polygon points="342,0 555,0 555,29 320,29" fill="var(--navy)"/>
    </svg>
    <p class="website">www.brindlewoodortho.com</p>
  </section>

</main>
</body>
</html>
```